Web re-design project for web software development agency

We need to re-design our existing website (www.tovenmedia.co.uk), and are going to start using a shorter domain (www.toven.com).
We have been in business for 8 years and it's time for an update.

We are based at Harrowmede Court (home of the code breakers). We specialise in writing software for the web. Over the years we have built up a healthy customer base and it is time to incorporate the features we build for our customers into our own site (e.g. social media).

We have a team of 8 talented developers with varied skills including: apps for mobile; complex server side software; front-end software; eCommerce software; specialised web based applications; integration software; hardware support; consultancy services. Our customers are diverse (e.g. banking; commerce; veterinary; R&D; health sector; law; accounting; film industry etc.).

Our current colour scheme is blue, white and green although we are not averse to moving away from these colours. We will also be dropping the DESIGN from our name and logo. Revised logo will be attached.

The site needs to be modern, sophisticated and leading edge. We want to show visitors to the site that we are a professional organisation.
Updates

Our logo in PSD format has been uploaded. Please drop the word DESIGN from the logo.

The deliverable for this project is a PSD (ideally we would like to see how the home page, portfolio page, resources page with mugshots, and forms are going to look).

Many thanks,
Tom

Please DO NOT include a Careers section 

We will also need a "meet our team" section with spaces for 10 photographs as well as some space underneath them so that we can add a short paragraph for each one of them.

Target Market(s)

Mainly large corporations needing bespoke web software, or generally complex projects (for anyone).

Industry/Entity Type

Software

Requirements
Must have
• We would like a home page designed that has the following elements on it:
- Show the new cookie compliance policy displayed probably in the top of the page (will disappear).
- A client Testimonial.
- Pricing icon.
- Social media Links.
- A Quote section in expand/collapse field as in (http://www.quillbrook-online.co.uk/our-services.shtml)

We would also like a portfolio page that showcases our clients in an interesting way.

Finally, we would like a form design that we can use throughout the site (i.e. how should buttons, radio buttons, checkboxes, dropdowns, text areas etc. look)?
Nice to have
• A page that follows these guidelines:
http://www.pagerivet.com/the-anatomy-of-a-perfect-landing-page

Here are a few examples of sites in our sector that we like:
- http://www.tidewell-studio.com/
- http://plinthos.co.uk/
- http://www.fernaxis.com/services/web-development (nice contact us page)
- http://www.quillbrook-online.co.uk/
- http://www.lumsa.com/
- http://www.netmoxa.co.uk/
Should not have
• No flash elemets. If anything, we will use html5.

```html
<!DOCTYPE html>
<html lang="en">
<head>
<meta charset="utf-8">
<title>Toven – Web Application Development and Support</title>
<link href="https://fonts.googleapis.com/css2?family=Open+Sans:ital,wght@0,400;0,600;0,700;1,400&display=swap" rel="stylesheet">
<style>
:root{
  --green:#7cb52b;
  --blue:#2a6fa8;
  --ink:#4a4a4a;
  --muted:#7a7a7a;
  --nav:#3b3b3b;
  --cookie:#4d5a3c;
  --panel:#f3f4f1;
  --line:#dcdcdc;
  --footer:#2f3030;
  --footer-base:#232424;
  --white:#fff;
}
*{box-sizing:border-box;margin:0;padding:0}
html,body{width:857px;height:1200px;overflow:hidden}
body{font-family:"Open Sans",Arial,sans-serif;color:var(--ink);background:var(--white);position:relative;font-size:10px;line-height:1.45}
a{color:inherit;text-decoration:none}

.site-header{position:absolute;left:0;top:0;width:857px;height:112px}
.brand{position:absolute;left:22px;top:22px;font-weight:600;font-size:24px;color:var(--nav)}
.main-nav{position:absolute;right:22px;top:66px;display:flex;background:var(--nav);border-radius:3px}
.main-nav a{color:var(--white);font-size:11px;padding:7px 17px;border-right:1px solid #555}
.main-nav a:last-child{border-right:0}
.main-nav a.active{background:var(--green);border-radius:3px 0 0 3px}

.cookie-bar{position:absolute;left:0;top:112px;width:857px;height:24px;background:var(--cookie);color:#e9eedf;font-size:9px;display:flex;align-items:center;padding:0 22px;justify-content:space-between}
.cookie-bar button{background:var(--green);color:var(--white);border:0;font:600 9px "Open Sans",sans-serif;padding:4px 10px;border-radius:2px}

.hero{position:absolute;left:0;top:136px;width:857px;height:250px;background:linear-gradient(#ffffff,#eef0ea);border-bottom:1px solid var(--line)}
.hero h1{position:absolute;left:22px;top:20px;width:400px;color:var(--green);font-size:29px;line-height:1.15;font-weight:600}
.hero .lead{position:absolute;left:22px;top:96px;width:380px;color:var(--blue);font-size:14px;line-height:1.3}
.hero .intro{position:absolute;left:22px;top:144px;width:360px;font-size:9px;color:var(--muted)}
.btn{display:inline-block;background:var(--green);color:var(--white);font-weight:600;font-size:11px;padding:6px 14px;border-radius:3px}
.hero .btn{position:absolute;left:22px;top:214px}
.hero-art{position:absolute;left:440px;top:22px;width:370px;height:196px;border-radius:6px;background:linear-gradient(135deg,#f6a23a,#e9622b 45%,#8cc43f)}
.quote-tab{position:absolute;right:47px;top:236px;background:var(--white);border:1px solid var(--line);border-top:0;padding:4px 16px;font-size:11px;color:var(--ink);border-radius:0 0 4px 4px}

.side-tabs{position:absolute;right:0;top:425px;width:20px}
.side-tabs span{display:block;writing-mode:vertical-rl;transform:rotate(180deg);color:var(--white);font-size:10px;font-weight:600;text-align:center}
.tab-share{background:var(--nav);padding:10px 0;margin-bottom:6px}
.tab-touch{background:var(--green);padding:22px 0}

.about{position:absolute;left:22px;top:468px;width:635px}
.about h2{position:absolute;left:0;top:14px;color:var(--green);font-size:15px;font-weight:600}
.about-photo{position:absolute;left:228px;top:0;width:150px;height:110px;background:linear-gradient(135deg,#f0a640,#d9552a)}
.about .text-side{position:absolute;left:393px;top:0;width:242px;font-size:9px;color:var(--muted)}
.about .text-wide{position:absolute;left:0;top:124px;width:635px;font-size:9px;color:var(--muted)}
.about .text-wide p{margin-bottom:8px}

.testimonials{position:absolute;left:672px;top:468px;width:164px;height:420px;background:var(--panel);border:1px solid var(--line);padding:10px 12px}
.testimonials h3{color:var(--green);font-size:14px;font-weight:600;margin-bottom:6px;display:flex;justify-content:space-between}
.testimonials h3 span{color:#bbb;font-size:22px;line-height:1}
.testimonials blockquote{font-style:italic;font-size:8.5px;color:var(--muted);margin-bottom:3px}
.testimonials cite{display:block;font-size:8px;color:#999;margin-bottom:12px}

.features{position:absolute;left:22px;top:905px;width:814px;display:flex;gap:16px}
.feature{flex:1;height:165px;background:var(--panel);border:1px solid var(--line);border-top:3px solid var(--green);padding:12px 14px}
.feature h3{color:var(--green);font-size:15px;font-weight:600;margin-bottom:8px}
.feature p{font-size:9px;color:var(--muted);margin-bottom:10px}
.feature a{color:var(--blue);font-size:9px;font-weight:600}

.site-footer{position:absolute;left:0;top:1088px;width:857px;height:112px;background:var(--footer);color:#cfcfcf}
.site-footer h4{color:var(--white);font-size:12px;font-weight:600;margin-bottom:6px}
.quick-links{position:absolute;left:22px;top:10px}
.quick-links .cols{display:flex;gap:40px}
.quick-links ul{list-style:none;font-size:8.5px}
.quick-links li{margin-bottom:2px}
.follow{position:absolute;left:470px;top:10px}
.follow ul{list-style:none;font-size:8.5px}
.follow li{display:flex;align-items:center;gap:6px;margin-bottom:4px}
.follow i{display:inline-block;width:11px;height:11px;border-radius:50%;background:var(--green)}
.footer-base{position:absolute;left:0;bottom:0;width:857px;height:20px;background:var(--footer-base);font-size:8px;padding:4px 22px;color:#aaa}
</style>
</head>
<body>

<header class="site-header">
  <div class="brand">Toven</div>
  <nav class="main-nav">
    <a href="#" class="active">Main</a><a href="#">About</a><a href="#">Services</a><a href="#">Technology</a><a href="#">Portfolio</a><a href="#">Jobs</a><a href="#">Contact</a>
  </nav>
</header>

<div class="cookie-bar">
  <span>This site uses cookies to store information on your computer. See our cookie policy for further details on how to block cookies</span>
  <button type="button">I am happy with this</button>
</div>

<section class="hero">
  <h1>Web Application Development and Support</h1>
  <p class="lead">Our Passion is developing complex application for the web that work for your and your business.</p>
  <p class="intro">Hollowbyte eSolutions is a web service company, offering a wide range of services which range from designing and development, that is covering almost all the fields in the best possible way.</p>
  <a href="#" class="btn">Learn More ›</a>
  <div class="hero-art" role="img" aria-label="Colourful illustration of web pages and devices"></div>
  <a href="#" class="quote-tab">Get a quote ›</a>
</section>

<div class="side-tabs">
  <span class="tab-share">Share</span>
  <span class="tab-touch">Get in touch</span>
</div>

<section class="about">
  <h2>Hollowbyte eSolutions</h2>
  <div class="about-photo" role="img" aria-label="Photo of the studio team at work"></div>
  <div class="text-side">
    <p>Hollowbyte eSolutions is a web service company, offering a wide range of services which range from designing and development, that is covering almost all the fields in the best possible way. A line that holds each bit of the process together and we work hard to present beautifully the working of the client's need and design.</p>
  </div>
  <div class="text-wide">
    <p>Few advantages he highlighted. We are in accordance with the industry verified processes to deliver the best to our clients all over the world. Over years we have built a strong reputation in providing website design and web development services.</p>
    <p>Thus, Marxist got ahead in the competition with other websites... Hollowbyte eSolutions provide you with an attractive and most convincing website to enhance your marketing grasp.</p>
    <p>The road to any success is through the right path and that's what we provide you. None of the other companies has the work we do. As close to the best, that's how you will be. We have don't go for the second best. Our expertise does not limit itself to web development but also it includes Web Hosting, Search Engine Optimization, E-Commerce. We partner hundreds of organizations to enhance their business, marketing and profit goals.</p>
  </div>
</section>

<aside class="testimonials">
  <h3>Testimonials <span>“</span></h3>
  <blockquote>Our Website Design team give an unforgettable impression on the customers and the visitors. We can assure you that this is the best place for requirements of your impelling website design solutions.</blockquote>
  <cite>- BT Author Name</cite>
  <blockquote>Hollowbyte eSolutions provides you the Search Engine Optimization making your website search engine friendly.</blockquote>
  <cite>- BT Author Name</cite>
  <blockquote>Hollowbyte eSolutions provides you the Search Engine Optimization making your website search engine friendly.</blockquote>
  <cite>- BT Author Name</cite>
  <blockquote>Hollowbyte eSolutions provides you the Search Engine Optimization making your website search engine friendly.</blockquote>
  <cite>- BT Author Name</cite>
</aside>

<section class="features">
  <article class="feature">
    <h3>Our Services</h3>
    <p>Hollowbyte eSolutions provides you the Search Engine Optimization making your website search engine friendly. So that the website can achieve top position.</p>
    <a href="#">READ MORE ›</a>
  </article>
  <article class="feature">
    <h3>Our Technology</h3>
    <p>Hollowbyte eSolutions provides you the Search Engine Optimization making your website search engine friendly. So that the website can achieve top position.</p>
    <a href="#">READ MORE ›</a>
  </article>
  <article class="feature">
    <h3>Our Work</h3>
    <p>Hollowbyte eSolutions provides you the Search Engine Optimization making your website search engine friendly. So that the website can achieve top position.</p>
    <a href="#">READ MORE ›</a>
  </article>
</section>

<footer class="site-footer">
  <div class="quick-links">
    <h4>Quick Links</h4>
    <div class="cols">
      <ul><li>Main Page</li><li>About Company</li><li>Services</li><li>Solutions</li></ul>
      <ul><li>Web Applications</li><li>Web Developments</li><li>Our Projects</li><li>Testimonials</li></ul>
      <ul><li>Support</li><li>Faq</li><li>Contact Us</li></ul>
    </div>
  </div>
  <div class="follow">
    <h4>Follow us</h4>
    <ul>
      <li><i></i>Follow us on Chatterline</li>
      <li><i></i>Connect with us on Facepage</li>
      <li><i></i>Network with us on Linkhub</li>
    </ul>
  </div>
  <div class="footer-base">© 2012 Company Name &nbsp;|&nbsp; All right reserved</div>
</footer>

</body>
</html>
```